Curavelloshop

We have roughly 50 items that we will be trading online. They are medical products aimed at the US and UK markets.

Most will be in cuboid boxes.

We would to have our own design that we could use across the product range.

Target Market(s)

Us and uk patients. Often 30+ years old

Industry/Entity Type

Medical

Requirements
Must have
• Our logo and space to have the medical in the centre of the box so it is clearly visible.
Nice to have
• Nice and simple colour scheme, nothing too bold.

```html
<!DOCTYPE html>
<html lang="en">
<head>
<meta charset="utf-8">
<title>Curavelloshop – Evening Primrose Oil Packaging</title>
<link rel="stylesheet" href="https://fonts.googleapis.com/css2?family=Roboto:wght@300;400;700&display=swap">
<style>
  :root {
    --bg: #dcebf0;
    --panel: #ffffff;
    --panel-edge: #d6dde0;
    --ink: #7d7d7d;
    --ink-soft: #a3a3a3;
    --rule: #7fd0e6;
    --brand: #2a86c9;
    --table-head: #6f6aa0;
    --table-row: #e6e3f2;
    --tone-peach: #f7dcc6;
    --tone-lilac: #e3ddf0;
    --tone-lime: #eef2d2;
    --tone-rose: #f5dada;
  }
  * { box-sizing: border-box; margin: 0; padding: 0; }
  html, body { width: 1200px; height: 905px; overflow: hidden; }
  body {
    background: var(--bg);
    font-family: "Roboto", Arial, sans-serif;
    color: var(--ink);
    position: relative;
  }
  .panel {
    position: absolute;
    background: var(--panel);
    border: 1px solid var(--panel-edge);
    overflow: hidden;
  }
  .panel--top   { left: 260px; top: 70px;  width: 340px; height: 320px; }
  .panel--front { left: 260px; top: 390px; width: 340px; height: 440px; }
  .panel--side  { left: 600px; top: 390px; width: 340px; height: 440px; }

  .brand-name {
    font-weight: 700;
    font-size: 15px;
    color: var(--brand);
    letter-spacing: -0.2px;
  }
  .panel--top .brand-name { position: absolute; right: 28px; top: 30px; }

  .product-name {
    font-weight: 300;
    font-size: 26px;
    color: var(--ink);
    letter-spacing: -0.3px;
    text-align: center;
  }
  .panel--top .product-name {
    position: absolute; left: 0; right: 0; top: 50%;
    transform: translateY(-50%);
  }
  .panel--front .product-name { position: absolute; left: 28px; right: 28px; top: 34px; }
  .name-rule {
    position: absolute; left: 60px; right: 60px; top: 78px;
    height: 1px; background: var(--rule);
  }
  .description {
    position: absolute; left: 34px; right: 34px; top: 96px;
    font-size: 11.5px; line-height: 1.6; font-weight: 300; color: var(--ink-soft);
    text-align: center;
  }

  .pattern-area {
    position: absolute; left: 24px; right: 24px; bottom: 26px; height: 168px;
    background: linear-gradient(120deg, var(--tone-peach), var(--tone-lilac) 35%, var(--tone-lime) 65%, var(--tone-rose));
  }

  .facts {
    position: absolute; left: 24px; top: 28px; width: 180px;
    border: 1px solid var(--table-head); font-size: 10px;
  }
  .facts__title {
    background: var(--table-head); color: #fff; font-weight: 700;
    padding: 5px 7px; font-size: 12px;
  }
  .facts__row { padding: 4px 7px; border-top: 1px solid #fff; color: #5f5b85; }
  .facts__row:nth-child(even) { background: var(--table-row); }
  .facts__row--split { display: flex; justify-content: space-between; }

  .side-brand { position: absolute; right: 24px; top: 30px; }
</style>
</head>
<body>
  <section class="panel panel--top" aria-label="Box lid">
    <span class="brand-name">Curavelloshop</span>
    <h2 class="product-name">evening primrose oil</h2>
  </section>

  <section class="panel panel--front" aria-label="Box front">
    <h1 class="product-name">evening primrose oil</h1>
    <div class="name-rule"></div>
    <p class="description">Evening Primrose Oil is a natural source of gamma-linolenic acid, an omega-6 fatty acid. Take one capsule daily with food as part of a balanced diet. Do not exceed the stated dose. Keep out of reach of children.</p>
    <div class="pattern-area" role="img" aria-label="Decorative pastel pattern of soft coloured circles"></div>
  </section>

  <section class="panel panel--side" aria-label="Box side">
    <div class="facts">
      <div class="facts__title">Supplement Facts</div>
      <div class="facts__row">Serving Size 1 Capsule</div>
      <div class="facts__row">Amount per serving</div>
      <div class="facts__row facts__row--split"><span>Evening Primrose Oil</span><span>1000mg</span></div>
      <div class="facts__row facts__row--split"><span>Gamma-linolenic acid</span><span>100mg</span></div>
      <div class="facts__row facts__row--split"><span>Vitamin E</span><span>10mg</span></div>
      <div class="facts__row">Other ingredients: gelatin, glycerin</div>
    </div>
    <span class="brand-name side-brand">Curavelloshop</span>
    <div class="pattern-area" role="img" aria-label="Decorative pastel pattern of soft coloured circles"></div>
  </section>
</body>
</html>
```